Flyer for a Unique Type of Tax Services

Please refer to the attached sample design for reference. Feel free to change the wording as needed. Here is the project brief:

Objective:
Objective of this flyer is to introduce our services which we are launching soon, which is new of a kind, to our potential customers i.e. online tax return preparation. By looking at the flyer we want our target audience to get convinced of our services and visit our website and register with us. They don’t have to pay anything to register.

Our Competitors:
Currently there are three main options available to get tax returns prepared. First is to buy tax software and get tax return prepared at own, this is the cheapest option. There are studies that suggest that people who are not well aware of tax laws there are chances they miss certain tax refunds by filing returns at their own and potentially lose money. Second option is to go to the local offices of nation-wide tax service companies like Pell & Varne and Morrow Tandy. They open offices only during tax season i.e. Jan through April but they are not available other part of the year and their association with the customers is temporary. Third option is to go to a CPA office which are the most expensive and very few people go for this option.

Weaknesses of the Current Options:
By self-preparing tax returns, there are chances that one can overlook certain tax laws that can provide additional tax credits and exemptions to people and overall they could have got a higher tax refund from the Govt. but they may miss it.
By going to other competitors during the peak time when tax returns are due, there are high chances that they don't have enough time to do research to ensure maximum refunds based on the exact circumstances of the individuals at the peak time as many people come to them during that time. Also they are not available after the tax season to provide them any answers to their questions or provide them tax planning tips to help them save tax in the next season.
By going to the CPA office, they charge a lot of fees and also for any tax advice later during the year, they will charge additional fees.

What we are offering:
We are offering a new option i.e. online tax return preparation through experts. We'll charge the fees competitive to what people are paying to local tax providers. But we will be different than our competitors as we'll be providing value added service if they got their returns prepared through us. Value added services we will be free of any additional cost for our customers who'll get tax return prepared through us.

Our Target Audience:
Our target audience is any person or couple who go to the tax service providers like Pell & Varne or Morrow Tandy to get their tax returns prepared.

How We are Different:
Here is the summary of the unique aspects of our business as compared to the competitors:
- Customers just pay us the price for preparing the annual return and price is comparable and competitive to what they have been paying to other providers.
- Unlike our competitors, we do extensive research to review the circumstances of our customers and explore applicable tax laws to make sure all available tax credits, exemptions, and deductions are taken for our customers, whereas our customers don't usually do such kind of research as during the peak tax season when customers approach them they usually don’t have time to do that kind of research. We start our association with our customers much sooner than the actual due date and this provides us time to do extensive research and we try our best that our customers could get higher tax returns.
- By just getting tax returns prepared through us, we enter into a long-term association with our customers and provide them complimentary tax planning tips throughout the year to help them save tax in the following year
- We are available to our customers year-round to provide complementary answers to any tax related questions without any additional cost e.g. how to save tax when buying a car, whether to buy or lease the care to save tax, for the sole-proprietor business how to save tax by using portion of the home as home-office, how to save tax by using personal car for personal business.
- We also provide answers to other basic financial advise related matters e.g. which insurance product is better, whether full insurance or term-life insurance to chose, how to save for the retirement etc.

Other Details:
Our logo has already been designed and we want the same logo to be used in the flyer. Our website address is: www.FiledRightPlus.com (it is still under construction but to get perspective of what we are trying to offer, visit this alternate website that it not final yet but will give an idea: http://www.filedrightplus.com/wordpress. Fyi, a video at this link is only a placeholder and not relevant to our services)

Requirements
Must have
• Please refer to the sample flyer attached. Feel free to change the design and language.
Should not have
• Please do not put any testimonial on the flyer as reflected in the under construction website.

```html
<!DOCTYPE html>
<html lang="en">
<head>
<meta charset="utf-8">
<title>FiledRight Plus – Tax Services Flyer</title>
<link href="https://fonts.googleapis.com/css2?family=Lato:wght@400;700;900&display=swap" rel="stylesheet">
<style>
  :root {
    --navy: #1f3a8f;
    --blue: #3b5bb5;
    --blue-deep: #2c4a9e;
    --red: #d9291c;
    --red-dark: #b81f15;
    --ink: #2b2b2b;
    --paper: #ffffff;
    --stage: #e4e4e4;
  }
  * { box-sizing: border-box; margin: 0; padding: 0; }
  html, body {
    width: 1200px; height: 968px; overflow: hidden;
    background: var(--stage);
    font-family: "Lato", Arial, sans-serif;
  }
  .flyer {
    position: absolute; left: 310px; top: 30px;
    width: 580px; height: 908px;
    background: var(--paper);
    box-shadow: 0 6px 24px rgba(0,0,0,.18);
    overflow: hidden;
  }
  /* header */
  .masthead { position: relative; height: 100px; }
  .masthead-tab {
    position: absolute; left: 32px; top: 0;
    width: 56px; height: 100px; background: var(--blue);
    display: flex; align-items: center; justify-content: center;
  }
  .brand {
    position: absolute; left: 104px; top: 32px;
    display: flex; align-items: center; gap: 10px;
  }
  .brand-mark { width: 16px; height: 16px; background: var(--red); border-radius: 50%; }
  .brand-name {
    font-weight: 900; font-size: 32px; color: var(--navy);
    letter-spacing: .5px; line-height: 1;
  }
  /* hero */
  .hero { position: relative; height: 300px; }
  .hero-backdrop { position: absolute; inset: 0; }
  .ribbon {
    position: absolute; color: #fff; background: var(--red);
    text-transform: uppercase; letter-spacing: 1.5px; white-space: nowrap;
    clip-path: polygon(0 0, 100% 0, 95% 100%, 0 100%);
  }
  .ribbon-top { top: 38px; left: 108px; width: 230px; height: 32px; font-size: 14px; line-height: 32px; padding-left: 42px; }
  .ribbon-main { top: 78px; left: 52px; width: 230px; height: 38px; font-size: 21px; line-height: 38px; padding-left: 32px; font-weight: 700; background: var(--red-dark); }
  .call-badge {
    position: absolute; left: 218px; top: 165px;
    width: 84px; height: 84px; border-radius: 50%;
    background: var(--blue);
    display: flex; flex-direction: column; align-items: center; justify-content: center;
    color: #fff;
  }
  .call-number { font-size: 8.5px; margin-top: 6px; letter-spacing: .3px; }
  /* body */
  .pitch { padding: 14px 30px 0; text-align: center; }
  .question {
    color: var(--navy); font-weight: 700; font-size: 17px; line-height: 1.22;
    margin-bottom: 8px;
  }
  .question em { font-style: normal; color: var(--red); }
  .kicker { color: var(--navy); font-weight: 700; font-size: 10.5px; letter-spacing: .5px; margin-top: 6px; }
  .section-title { color: var(--red); font-weight: 700; font-size: 19px; letter-spacing: 1.5px; margin-bottom: 6px; line-height: 1.1; }
  .details p { font-size: 8.3px; line-height: 1.4; color: var(--ink); margin-bottom: 7px; }
  .cta {
    display: flex; align-items: center; justify-content: center; gap: 12px;
    margin-top: 10px; color: var(--navy); font-weight: 700;
  }
  .cta-label { font-size: 15px; letter-spacing: 2px; }
  .cta-url { font-size: 14px; letter-spacing: .8px; }
</style>
</head>
<body>
<main class="flyer">
  <header class="masthead">
    <div class="masthead-tab">
      <svg width="26" height="30" viewBox="0 0 26 30" fill="none" stroke="#fff" stroke-width="3">
        <polyline points="3,4 13,13 23,4"/>
        <polyline points="3,15 13,24 23,15"/>
      </svg>
    </div>
    <div class="brand">
      <span class="brand-mark"></span>
      <span class="brand-name">FiledRight Plus</span>
    </div>
  </header>

  <section class="hero">
    <svg class="hero-backdrop" width="580" height="300" viewBox="0 0 580 300">
      <defs>
        <linearGradient id="photoTone" x1="0" y1="0" x2="1" y2="1">
          <stop offset="0" stop-color="#5a5a5a"/>
          <stop offset=".6" stop-color="#3a3a3a"/>
          <stop offset="1" stop-color="#2a2a2a"/>
        </linearGradient>
      </defs>
      <rect width="580" height="300" fill="#2c4a9e"/>
      <polygon points="390,0 580,0 580,300 0,300" fill="url(#photoTone)"
               role="img" aria-label="Photo of a smiling businesswoman holding a blue umbrella against a dark wall printed with the word tax"/>
    </svg>
    <div class="ribbon ribbon-top">Our priority is</div>
    <div class="ribbon ribbon-main">Your success</div>
    <div class="call-badge">
      <svg width="24" height="24" viewBox="0 0 24 24" fill="#fff">
        <path d="M6.6 10.8a15.1 15.1 0 0 0 6.6 6.6l2.2-2.2c.3-.3.7-.4 1-.2 1.1.4 2.3.6 3.6.6.6 0 1 .4 1 1V20c0 .6-.4 1-1 1A17 17 0 0 1 3 4c0-.6.4-1 1-1h3.5c.6 0 1 .4 1 1 0 1.3.2 2.5.6 3.6.1.3 0 .7-.2 1z"/>
      </svg>
      <span class="call-number">+(123) 555 0187</span>
    </div>
  </section>

  <section class="pitch">
    <h2 class="question">Does your Tax Return Prepare has time to do <em>Extensive Research</em> for you to help you get <em>maximum refunds</em>?</h2>
    <h2 class="question">Do you get year-round <em>Free Advice</em> regarding your <em>Tax related Questions</em> from your exiting Tax Service Provider?</h2>
    <h2 class="question">Does your existing Tax Service Provider give you <em>Complementary Tax Planning Tips</em> throughout the year to help you <em>save tax</em> in the following year?</h2>

    <p class="kicker">YOU SHOULD KNOW</p>
    <h3 class="section-title">HOW WE ARE DIFFERENT</h3>

    <div class="details">
      <p>Customers just pay us the price for preparing the annual return and price is comparable and competitive to what they have been paying to other providers.</p>
      <p>Unlike our competitors, we do extensive research to review the circumstances of our customers and explore applicable tax laws to make sure all available tax credits, exemptions, and deductions are taken for our customers, whereas our customers don't usually do such kind of research as during the peak tax season when customers approach them they usually don't have time to do that kind of research. We start our association with our customers much sooner than the actual due date and this provides us time to do extensive research and we try our best that our customers could get higher tax returns.</p>
      <p>By just getting tax returns prepared through us, we enter into a long-term association with our customers and provide them complimentary tax planning tips throughout the year to help them save tax in the following year</p>
      <p>We are available to our customers year-round to provide complementary answers to any tax related questions without any additional cost e.g. how to save tax when buying a car, whether to buy or lease the care to save tax, for the sole-proprietor business how to save tax by using portion of the home as home-office, how to save tax by using personal car for personal business.</p>
      <p>We also provide answers to other basic financial advise related matters e.g. which insurance product is better, whether full insurance or term-life insurance to chose, how to save for the retirement etc.</p>
    </div>

    <div class="cta">
      <span class="cta-label">Register Now Free at</span>
      <svg width="24" height="20" viewBox="0 0 24 20" fill="none" stroke="#1f3a8f" stroke-width="2">
        <rect x="1" y="1" width="22" height="14" rx="1"/>
        <line x1="12" y1="15" x2="12" y2="19"/>
        <line x1="7" y1="19" x2="17" y2="19"/>
      </svg>
      <span class="cta-url">www.FiledRightPlus.com</span>
    </div>
  </section>
</main>
</body>
</html>
```